Innovative Consulting Firm Needs New Business Cards and Stationary

Our Innovative Consulting Firm, Larkfield Consulting, is in need of new business cards and stationary designs. We want two-sided cards that incorporate our logo, which is attached. We are looking for something not too formal, but is professional and slick.

Card should have the following information:
Name (ex. Tom Bradley)
Title (ex. Manager)
Address (ex. 24680 Cedar Lane)
Address 2 (ex. Suite 100)
City
State
Zip Code
Mobile
Email

The card should also have our website: www.larkfieldconsulting.example

Industry/Entity Type

Management Consulting

Contact Information for Business Card

Name (ex. Tom Bradley)
Title (ex. Manager)
Address 2 (ex. Suite 100)
City
State
Zip Code
Mobile
Email

Font styles to use
Sans Serif

Requirements
Must have
• The colors on the card must match the colors in the logo. The exact color codes are attached in a pdf.
Nice to have
• The Company's Tagline is "Focused on your Future". This might be nice to incorporate, but not necessary.

```html
<!DOCTYPE html>
<html lang="en">
<head>
<meta charset="utf-8">
<title>Larkfield Consulting – Business Card</title>
<link rel="stylesheet" href="https://fonts.googleapis.com/css2?family=Lato:wght@400;700&display=swap">
<style>
  :root {
    --navy: #1f4d7c;
    --band-blue: #24527f;
    --accent-orange: #f0ab2e;
    --card-white: #ffffff;
    --backdrop: #3a3838;
    --ink-white: #ffffff;
  }
  * { margin: 0; padding: 0; box-sizing: border-box; }
  html, body {
    width: 1200px; height: 810px; overflow: hidden;
    background: var(--backdrop);
    font-family: "Lato", Arial, sans-serif;
  }
  .sheet {
    position: relative; width: 1200px; height: 810px;
    display: flex; justify-content: center; align-items: center; gap: 30px;
  }
  .card {
    position: relative; width: 560px; height: 320px;
    background: var(--card-white); border-radius: 16px; overflow: hidden;
    box-shadow: 0 10px 24px rgba(0,0,0,0.35);
  }
  .wordmark {
    display: flex; align-items: center; gap: 10px;
    color: var(--navy); font-weight: 700; white-space: nowrap;
  }
  .wordmark-dot {
    width: 16px; height: 16px; border-radius: 50%;
    background: var(--accent-orange); flex: none;
  }
  /* Front */
  .card-front .wordmark {
    position: absolute; left: 0; right: 0; top: 118px;
    justify-content: center; font-size: 38px;
  }
  .card-front .web-band {
    position: absolute; left: 0; right: 0; bottom: 0; height: 50px;
    background: var(--band-blue); color: var(--ink-white);
    display: flex; align-items: center; justify-content: center;
    font-size: 15px; font-weight: 700; letter-spacing: 1px;
  }
  /* Back */
  .card-back .wordmark {
    position: absolute; right: 28px; top: 34px; font-size: 26px;
  }
  .card-back .sweep { position: absolute; inset: 0; }
  .person { position: absolute; left: 40px; top: 182px; }
  .person-name {
    color: var(--navy); font-size: 18px; font-weight: 400; letter-spacing: 0.5px;
  }
  .person-title { color: var(--accent-orange); font-size: 13px; margin-top: 2px; }
  .contact {
    position: absolute; right: 24px; top: 176px;
    color: var(--ink-white); font-size: 12px; line-height: 19px; text-align: right;
    list-style: none; white-space: nowrap;
  }
  .contact li { display: flex; justify-content: flex-end; align-items: center; gap: 6px; }
  .contact .spacer { height: 8px; }
  .contact svg { width: 11px; height: 11px; flex: none; }
  .notch {
    position: absolute; left: -6px; top: 150px; width: 14px; height: 22px;
    background: var(--band-blue); border-radius: 0 8px 8px 0;
  }
</style>
</head>
<body>
<main class="sheet">
  <section class="card card-front" aria-label="Card front">
    <div class="wordmark"><span class="wordmark-dot"></span>Larkfield Consulting</div>
    <div class="web-band">www.larkfieldconsulting.example</div>
  </section>

  <section class="card card-back" aria-label="Card back">
    <svg class="sweep" viewBox="0 0 560 320" aria-hidden="true">
      <path d="M188 320 Q268 112 560 72 L560 320 Z" fill="var(--accent-orange)"/>
      <path d="M210 320 Q290 122 560 86 L560 320 Z" fill="var(--card-white)"/>
      <path d="M214 320 Q294 126 560 90 L560 320 Z" fill="var(--band-blue)"/>
    </svg>
    <div class="notch"></div>
    <div class="wordmark"><span class="wordmark-dot"></span>Larkfield Consulting</div>
    <div class="person">
      <div class="person-name">TOM BRADLEY</div>
      <div class="person-title">Manager</div>
    </div>
    <ul class="contact">
      <li>24680 Cedar Lane</li>
      <li>Suite 100, City, State, Zip Code 1005</li>
      <li class="spacer"></li>
      <li>(000) 0000 0000
        <svg viewBox="0 0 12 12"><path d="M2.5 1 L4.5 1 L5.2 3.4 L4 4.4 Q5 6.8 7.6 8 L8.6 6.8 L11 7.5 L11 9.5 Q10.6 11 9 11 Q1 10 1 2.6 Q1 1 2.5 1 Z" fill="#fff"/></svg>
      </li>
      <li>info@larkfieldconsulting.example
        <svg viewBox="0 0 12 12"><rect x="1" y="2.5" width="10" height="7" fill="#fff"/><path d="M1 2.5 L6 6.5 L11 2.5" fill="none" stroke="var(--band-blue)" stroke-width="1"/></svg>
      </li>
      <li>www.larkfieldconsulting.example
        <svg viewBox="0 0 12 12"><circle cx="6" cy="6" r="5" fill="#fff"/><path d="M1 6 H11 M6 1 Q3 6 6 11 M6 1 Q9 6 6 11" fill="none" stroke="var(--band-blue)" stroke-width="0.8"/></svg>
      </li>
    </ul>
  </section>
</main>
</body>
</html>
```